HVAC company business card design

We need a business card design for a HVAC company. The design must look professional. Both sides will be used. The total data to be on the business card is
Name
Position
Email
Direct Phone/Moile Phone
Company Contacts /Address, Phone, Fax, web)
All data will be submit once the design is confirmed. For generic purposes use;
Emre Toksoy
Managing Director
+902324815263 (Mobile)
4712 Sokak No: 9 KBSE Yenikent IZMIR TURKEY
Tel: +902324815263 Fax : +902324815269
www.luvon.com.tr

Target Market(s)

HVAC

Industry/Entity Type

Business

Contact Information for Business Card

The total data to be on the business card is
Name
Position
Email
Direct Phone/Moile Phone
Emre Toksoy
Managing Director
+902324815263 (Mobile)
www.luvon.com.tr
The BC will use both sides of the card. The front will include the full logo and the details for the business card holder. The business card can be divided into vertical/horizontal or to a special shape. The common data like the company address/phone/fax should be indicated elsewehere. The back can contain some part or the whole logo and must contain the web address.

Font styles to use
Serif
Sans Serif

Colors
0355a3
cfdfed

Requirements
Should not have
• Please be careful with the fonts, it shouldnt be too small or too big and must not interfere with the logo fonts. If you need to use a curvy shape please do not use as the logo is already curvy or use the curves from the logo (if it looks good, otherwise forget it)
• We are not in favor of pictograms, only if they are perfect use them.

```html
<!DOCTYPE html>
<html lang="en">
<head>
<meta charset="utf-8">
<title>Luvon business card</title>
<link rel="stylesheet" href="https://fonts.googleapis.com/css2?family=Open+Sans:wght@400;600;700&display=swap">
<style>
  :root {
    --backdrop: #000000;
    --card: #2f3034;
    --card-edge: #3a3b40;
    --brand-blue: #3a8be0;
    --deep-blue: #0355a3;
    --text-light: #e8ebef;
    --divider: #45474c;
  }
  * { margin: 0; padding: 0; box-sizing: border-box; }
  html, body {
    width: 1200px; height: 900px; overflow: hidden;
    background: var(--backdrop);
    font-family: "Open Sans", Arial, sans-serif;
    color: var(--text-light);
  }
  .canvas { position: relative; width: 1200px; height: 900px; }
  .card {
    position: absolute; top: 271px;
    width: 457px; height: 281px;
    background: var(--card);
    border-radius: 14px;
    box-shadow: inset 0 0 0 1px var(--card-edge);
  }
  .card--front { left: 137px; }
  .card--back { left: 627px; }

  .front-mark {
    position: absolute; left: 58px; top: 84px; width: 128px;
    display: flex; flex-direction: column; align-items: center; gap: 10px;
  }
  .mark-dot {
    width: 76px; height: 76px; border-radius: 50%;
    background: var(--brand-blue);
  }
  .mark-name {
    font-size: 20px; font-weight: 600; letter-spacing: 2px; color: var(--text-light);
  }
  .divider {
    position: absolute; left: 224px; top: 94px;
    width: 1px; height: 120px; background: var(--divider);
  }
  .holder { position: absolute; left: 251px; top: 59px; }
  .holder-name { font-size: 15px; font-weight: 600; color: var(--brand-blue); line-height: 20px; }
  .holder-role { font-size: 12.5px; line-height: 17px; }
  .address { position: absolute; left: 251px; top: 115px; font-size: 12.5px; line-height: 19px; }
  .contacts { position: absolute; left: 251px; top: 168px; list-style: none; font-size: 12.5px; }
  .contacts li { display: flex; align-items: center; height: 19px; }
  .contacts svg { width: 10px; height: 10px; margin-right: 12px; fill: var(--brand-blue); }

  .back-logo {
    position: absolute; left: 92px; top: 100px;
    display: flex; align-items: center; gap: 22px;
  }
  .back-logo .mark-dot { width: 84px; height: 84px; }
  .back-logo .mark-name { font-size: 58px; font-weight: 600; letter-spacing: 3px; }
  .web {
    position: absolute; left: 0; right: 0; top: 223px;
    text-align: center; font-size: 16px; font-weight: 700; letter-spacing: 3px;
  }
</style>
</head>
<body>
<main class="canvas">
  <section class="card card--front" aria-label="Card front">
    <div class="front-mark">
      <span class="mark-dot"></span>
      <span class="mark-name">LUVON</span>
    </div>
    <span class="divider"></span>
    <div class="holder">
      <p class="holder-name">Emre Toksoy</p>
      <p class="holder-role">Managing Director</p>
    </div>
    <p class="address">4712 Sokak No: 9 KBSE<br>Yenikent IZMIR TURKEY</p>
    <ul class="contacts">
      <li><svg viewBox="0 0 10 10" aria-label="Mobile"><path d="M2.5 0h5a1 1 0 0 1 1 1v8a1 1 0 0 1-1 1h-5a1 1 0 0 1-1-1V1a1 1 0 0 1 1-1zm.5 1.5v6h4v-6z"/></svg>+902324815263</li>
      <li><svg viewBox="0 0 10 10" aria-label="Phone"><path d="M2 0.5l1.8 2-0.9 1.3c.6 1.3 1.6 2.3 2.9 2.9l1.3-.9 2 1.8-1.2 1.8C4.3 9.4.6 5.7.2 1.7z"/></svg>&nbsp;+902324815263</li>
      <li><svg viewBox="0 0 10 10" aria-label="Fax"><path d="M2.5 0h4l1 1v2h-5zM1 3.5h8a1 1 0 0 1 1 1V10H0V4.5a1 1 0 0 1 1-1zm2 3.5v1.5h4V7z"/></svg>+902324815269</li>
      <li><svg viewBox="0 0 10 10" aria-label="Email"><path d="M0 2h10v1L5 6 0 3zm0 2.2l5 3 5-3V8.5H0z"/></svg>&nbsp;info@luvon.com.tr</li>
    </ul>
  </section>

  <section class="card card--back" aria-label="Card back">
    <div class="back-logo">
      <span class="mark-dot"></span>
      <span class="mark-name">LUVON</span>
    </div>
    <p class="web">www.luvon.com.tr</p>
  </section>
</main>
</body>
</html>
```